Multi-Faceted Legal and Finanacial Advisory Group Needs Business Card Design

We need a business card design for a newly branded Orlando Florida area advising group consisting of Attorneys, Accountants and Financial Planners. The company is named RT Counsel Group. You will find our initial work on a business card. The information on the business card are merely guideposts and not final product. The logo does not have the be the same as provided since we have not finalized the logo. We would like to stay with a black/white/grey color scheme, but limited use of color is not out of the question.

Target Market(s)

Businesses and their Corporate Representatives

Industry/Entity Type

Business

Contact Information for Business Card

Should have Name, Title, Phone, Cell, Fax, Email and website. Logo should incorporate RT in some fashion however final logo used does not have to be the one on the document provided.

Requirements
Must have
• An RT design on front and back.

```html
<!DOCTYPE html>
<html lang="en">
<head>
<meta charset="utf-8">
<title>RT Counsel Group – Business Card</title>
<link href="https://fonts.googleapis.com/css2?family=Source+Sans+3:wght@400;600&family=Tinos&display=swap" rel="stylesheet">
<style>
  :root {
    --stage: #161616;
    --card-front: #ffffff;
    --card-back: #e2e2e2;
    --ink: #4a4a4a;
    --ink-soft: #9a9a9a;
    --ink-dark: #111111;
    --mark-fill: #ececec;
  }
  * { margin: 0; padding: 0; box-sizing: border-box; }
  html, body { width: 1200px; height: 900px; overflow: hidden; }
  body {
    background: var(--stage);
    position: relative;
    font-family: "Source Sans 3", "Myriad Pro", Arial, sans-serif;
  }
  .card {
    position: absolute;
    width: 436px;
    height: 253px;
    border-radius: 14px;
  }
  .card--front { left: 150px; top: 306px; background: var(--card-front); }
  .card--back  { left: 629px; top: 308px; background: var(--card-back); }

  .front-mark {
    position: absolute;
    left: 55px; top: 76px;
    width: 118px; height: 104px;
    border: 2px solid var(--ink);
    background: var(--mark-fill);
  }

  .contact { position: absolute; left: 211px; top: 47px; color: var(--ink); }
  .contact__name { font-size: 19px; font-weight: 600; line-height: 24px; }
  .contact__title { font-size: 13px; color: var(--ink-soft); line-height: 16px; }
  .contact__address { margin-top: 10px; font-size: 13px; line-height: 14px; }
  .contact__list { list-style: none; margin-top: 13px; font-size: 13px; }
  .contact__list li { display: flex; align-items: center; height: 16.5px; }
  .contact__list svg { width: 9px; height: 9px; margin-right: 7px; fill: var(--ink); }

  .back-brand {
    position: absolute;
    left: 38px; top: 80px;
    display: flex; align-items: flex-start;
  }
  .back-brand__square {
    width: 93px; height: 80px;
    border: 2px solid var(--ink-dark);
    margin-right: 12px;
  }
  .back-brand__text {
    font-family: "Tinos", "Times New Roman", serif;
    color: var(--ink-dark);
    margin-top: 22px;
  }
  .back-brand__name { font-size: 32px; line-height: 36px; white-space: nowrap; }
  .back-brand__services { font-size: 8px; text-align: center; margin-top: 7px; white-space: nowrap; }
</style>
</head>
<body>
  <section class="card card--front">
    <div class="front-mark" role="img" aria-label="RT Counsel Group brand mark placeholder"></div>
    <div class="contact">
      <div class="contact__name">Marcus Ellery</div>
      <div class="contact__title">Managing Director</div>
      <div class="contact__address">1234, Address Goes Here<br>Country Name, 123456</div>
      <ul class="contact__list">
        <li><svg viewBox="0 0 10 10"><path d="M1 4 Q5 0 9 4 L8 5 L6.5 4 L6.5 3 Q5 2.5 3.5 3 L3.5 4 L2 5 Z M2.5 6 H7.5 V9 H2.5 Z"/></svg>123-456-7890</li>
        <li><svg viewBox="0 0 10 10"><path d="M3 1 H7 V3 H9 V9 H1 V3 H3 Z M4 2 V3 H6 V2 Z M2.5 5 V6 H4 V5 Z M5 5 V6 H7.5 V5 Z"/></svg>123-456-7890</li>
        <li><svg viewBox="0 0 10 10"><path d="M1 2.5 H9 V8 H1 Z M1.5 3 L5 5.5 L8.5 3 Z" fill-rule="evenodd"/></svg>info@youremail.com</li>
        <li><svg viewBox="0 0 10 10"><path d="M4 6 L6 4 M3 5 L1.8 6.2 A1.6 1.6 0 0 0 3.8 8.2 L5 7 M7 5 L8.2 3.8 A1.6 1.6 0 0 0 6.2 1.8 L5 3" stroke="#4a4a4a" stroke-width="1.1" fill="none"/></svg>www.yourweb.com</li>
      </ul>
    </div>
  </section>

  <section class="card card--back">
    <div class="back-brand">
      <div class="back-brand__square"></div>
      <div class="back-brand__text">
        <div class="back-brand__name">RT Counsel Group</div>
        <div class="back-brand__services">Attorneys • Accountants • Financial Planners</div>
      </div>
    </div>
  </section>
</body>
</html>
```